All-Natural Head Lice Removal company

I need a business card with my pre-existing logo. We are a new company located in Portland Oregon that goes into peoples homes to help with head lice removal. My products and approach are all- natural and also will be around children.On my current logo we used Teal Bl and the color Green. I am open to new ideas just want it simple and creative

Target Market(s)

my biggest market is families of school aged children

Industry/Entity Type

Business

Contact Information for Business Card

see upload for details from previous business card

Font styles to use
Serif

Colors
33a6d7
9bcb3b
f37122

Requirements
Must have
• Basic information/ logo put into a creative format that is catching to the eye
Nice to have
• creative

```html
<!DOCTYPE html>
<html lang="en">
<head>
<meta charset="utf-8">
<title>Nit Scout – Business Card</title>
<link href="https://fonts.googleapis.com/css2?family=Open+Sans:wght@400;600;700;800&display=swap" rel="stylesheet">
<style>
  :root {
    --green: #7dc242;
    --teal: #33a6d7;
    --ink: #1a1a1a;
    --paper: #ffffff;
    --paper-grey: #eeeeee;
    --backdrop: #e7e4df;
    --card-w: 680px;
    --card-h: 390px;
  }
  * { box-sizing: border-box; margin: 0; padding: 0; }
  html, body { width: 1200px; height: 1023px; overflow: hidden; }
  body {
    background: var(--backdrop);
    font-family: "Open Sans", sans-serif;
    color: var(--ink);
    position: relative;
  }
  .card {
    position: absolute;
    width: var(--card-w);
    height: var(--card-h);
    border-radius: 26px;
    overflow: hidden;
    box-shadow: 0 10px 28px rgba(0,0,0,.18);
  }
  .card-front { left: 260px; top: 70px; background: var(--paper); }
  .card-back {
    left: 260px; top: 560px;
    background: radial-gradient(ellipse at 40% 35%, #ffffff 0%, var(--paper-grey) 100%);
  }

  /* wordmark */
  .wordmark { display: flex; align-items: center; gap: 12px; }
  .wordmark-dot {
    flex: none;
    width: 62px; height: 62px; border-radius: 50%;
    background: var(--green);
  }
  .wordmark-name {
    font-weight: 800; font-size: 46px; color: var(--ink);
    letter-spacing: -.5px; white-space: nowrap;
  }

  /* front */
  .front-identity { position: absolute; left: 70px; top: 70px; }
  .person { margin-top: 22px; padding-left: 74px; }
  .person-name { color: var(--green); font-weight: 700; font-size: 24px; }
  .person-role { font-weight: 700; font-size: 14px; margin-top: 2px; }

  .contact-band {
    position: absolute; left: 0; bottom: 0;
    width: 100%; height: 150px;
  }
  .band-shape { position: absolute; inset: 0; }
  .contact-list {
    position: absolute; left: 200px; right: 24px; top: 28px;
    display: flex; justify-content: space-between;
    list-style: none;
  }
  .contact-item {
    display: flex; flex-direction: column; align-items: center; gap: 12px;
    color: #fff; font-size: 15px; white-space: nowrap;
  }
  .contact-icon {
    width: 42px; height: 42px; border-radius: 50%;
    display: flex; align-items: center; justify-content: center;
    border: 3px solid #fff;
  }
  .contact-icon svg { display: block; }
  .icon-phone { background: var(--green); }
  .icon-mail { background: var(--ink); }
  .icon-web { background: var(--teal); }

  /* back */
  .back-content {
    position: absolute; left: 44px; right: 44px; top: 0; bottom: 0;
    display: flex; align-items: center; justify-content: space-between; gap: 30px;
  }
  .back-message {
    font-size: 15px; line-height: 1.5; color: var(--ink); white-space: nowrap;
  }
  .back-message .site-name { color: var(--teal); }
  .back-logo .wordmark-dot { width: 44px; height: 44px; }
  .back-logo .wordmark-name { font-size: 30px; }
</style>
</head>
<body>

<section class="card card-front" aria-label="Business card front">
  <div class="front-identity">
    <div class="wordmark">
      <span class="wordmark-dot"></span>
      <span class="wordmark-name">Nit Scout</span>
    </div>
    <div class="person">
      <p class="person-name">Maren Holloway</p>
      <p class="person-role">Owner</p>
    </div>
  </div>

  <div class="contact-band">
    <svg class="band-shape" width="680" height="150" viewBox="0 0 680 150" aria-hidden="true">
      <polygon points="200,0 680,0 680,150 140,150" fill="var(--green)"/>
    </svg>
    <ul class="contact-list">
      <li class="contact-item">
        <span class="contact-icon icon-phone">
          <svg width="20" height="20" viewBox="0 0 24 24" aria-hidden="true"><path d="M6.6 10.8a15 15 0 0 0 6.6 6.6l2.2-2.2c.3-.3.7-.4 1-.2 1.1.4 2.3.6 3.6.6.6 0 1 .4 1 1V20c0 .6-.4 1-1 1A17 17 0 0 1 3 4c0-.6.4-1 1-1h3.5c.6 0 1 .4 1 1 0 1.3.2 2.5.6 3.6.1.3 0 .7-.2 1z" fill="#fff"/></svg>
        </span>
        <span>+353 87 5550142</span>
      </li>
      <li class="contact-item">
        <span class="contact-icon icon-mail">
          <svg width="20" height="16" viewBox="0 0 24 18" aria-hidden="true"><rect x="1" y="1" width="22" height="16" rx="1" fill="none" stroke="#fff" stroke-width="2"/><path d="M1 1l11 9 11-9" fill="none" stroke="#fff" stroke-width="2"/></svg>
        </span>
        <span>+353 87 5550142</span>
      </li>
      <li class="contact-item">
        <span class="contact-icon icon-web">
          <svg width="22" height="22" viewBox="0 0 24 24" aria-hidden="true"><g fill="none" stroke="#fff" stroke-width="1.6"><circle cx="12" cy="12" r="10"/><ellipse cx="12" cy="12" rx="4.5" ry="10"/><path d="M2 12h20M4 6.5h16M4 17.5h16"/></g></svg>
        </span>
        <span>hello@nitscoutcare.com</span>
      </li>
    </ul>
  </div>
</section>

<section class="card card-back" aria-label="Business card back">
  <div class="back-content">
    <p class="back-message">
      Try Nit Scout Today and Be Lice Free Tomorrow!<br>
      All Natural In-Home Lice Removal Servise<br>
      www.<span class="site-name">NitScout</span>.com
    </p>
    <div class="back-logo wordmark">
      <span class="wordmark-dot"></span>
      <span class="wordmark-name">Nit Scout</span>
    </div>
  </div>
</section>

</body>
</html>
```